Subscription box needs a bold design for our lock front mailer box

We are a new subscription box service called Petal Crest Box filled with an array of delightful products made by women artisans and business owners. Products include handcrafted bath, beauty and spa products, gourmet delights, home and lifestyle goods, jewelry and accessories. We also place great importance on obtaining organic products from sustainable sources where possible.
Our focus is on lifting women up and on inspiring our customers to do so too. We do this by sourcing all of our products from women, creating a monthly “Kind Turn” card for each box with ideas on how to give another woman a boost, and donating 10% of our proceeds to a woman-focused charity each month. We believe that we will all be stronger if we work together.
We need a bold design for our mailing box that incorporates our logo, our website address, our tag line and possibly our mascot.
The box will be white with red print. We have a template for PDF and EPS from the company we will use to produce the boxes. We are attaching templates, logo, mascot photo, sample pattern and ideas. We would like a designer that can bring their own ideas and we are very open to new thoughts.

Target Market(s)

Women, 25 to 65. Educated with significant disposable income.

Industry/Entity Type

Business

Colors
ec1f27

Requirements
Must have
• A bold look. Must include our logo and tag line "Uplift Yourself, Kind Turn Women"
• Will be red print on a white box.
Nice to have
• Have included file with ideas but am very open to other thoughts and designs.

```html
<!DOCTYPE html>
<html lang="en">
<head>
<meta charset="utf-8">
<title>Petal Crest Box – Mailer Box Dieline</title>
<link href="https://fonts.googleapis.com/css2?family=Montserrat:wght@400;500;600;800&family=Kristi&family=Allura&display=swap" rel="stylesheet">
<style>
  :root{
    --bg:#929191;
    --flap:#999898;
    --white:#ffffff;
    --red:#ec1f27;
    --ink:#111111;
    --pattern-light:#e4e4e4;
    --pattern-mid:#c9c9c9;
    --tab:#5e5e5e;
  }
  *{margin:0;padding:0;box-sizing:border-box}
  html,body{width:1200px;height:883px;overflow:hidden;background:var(--bg)}
  .canvas{position:relative;width:1200px;height:883px;font-family:"Montserrat",sans-serif}
  .dieline{position:absolute;left:0;top:0}
  .panel{position:absolute}
  .white{background:var(--white)}
  .red{background:var(--red);color:var(--white)}

  /* lid end panels */
  .end-copy{position:absolute;left:21px;width:142px;font-size:8.8px;font-weight:500;line-height:12.4px}
  .end-copy .line{display:block;white-space:nowrap;text-align:justify;text-align-last:justify}
  .end-copy .line.last{text-align-last:left}
  .end-top .end-copy{top:34px;transform:rotate(180deg)}
  .end-bottom .site{position:absolute;top:26px;width:100%;text-align:center;font-size:9.6px;font-weight:600}
  .end-bottom .end-copy{top:50px}

  /* left side panel */
  .mascot{position:absolute;left:24px;top:26px;width:78px;height:54px;border-radius:40%;
    background:radial-gradient(circle at 55% 50%,#dcdcdc 0,#f3f3f3 70%)}
  .side-note{position:absolute;left:56px;top:172px;width:156px;height:38px;border:1px solid #999;
    transform:translate(-50%,-50%) rotate(90deg);padding:4px 6px;
    font-size:6.2px;line-height:1.3;color:var(--red);font-weight:600;text-align:justify}

  /* lid */
  .pattern{position:absolute;inset:0}
  .lid-pattern{background:linear-gradient(135deg,var(--pattern-light),var(--pattern-mid))}
  .front-pattern{background:linear-gradient(135deg,var(--pattern-mid),var(--pattern-light))}
  .label-area{position:absolute;background:var(--white);border:2px solid var(--red)}
  .label-text{position:absolute;left:50%;top:50%;font-family:"Kristi",cursive;font-size:44px;line-height:0.85;color:var(--ink);
    transform:translate(-50%,-50%) rotate(-90deg);white-space:nowrap;text-align:center}

  /* back side */
  .site-vertical{position:absolute;left:59px;top:132px;font-size:10.5px;font-weight:600;letter-spacing:1px;color:var(--red);
    transform:translate(-50%,-50%) rotate(-90deg);white-space:nowrap}
  .rule{position:absolute;left:58px;width:2px;background:var(--red)}

  /* front */
  .brand-label{position:absolute;background:var(--white);border:3px solid var(--red)}
  .brand-name{position:absolute;left:50%;top:50%;font-weight:800;font-size:19px;color:var(--ink);letter-spacing:0.4px;
    transform:translate(-50%,-50%) rotate(-90deg);white-space:nowrap}

  /* tagline side */
  .tagline-box{position:absolute;left:40px;top:48px;width:62px;height:176px;border:1px solid var(--red)}
  .tagline{position:absolute;left:50%;top:50%;width:172px;height:58px;
    transform:translate(-50%,-50%) rotate(-90deg);display:flex;flex-direction:column;justify-content:center;padding:0 6px}
  .tagline-script{font-family:"Allura",cursive;font-size:27px;color:var(--red);line-height:1;white-space:nowrap}
  .tagline-sub{font-size:9.5px;font-weight:500;color:var(--ink);white-space:nowrap;align-self:flex-end;margin-top:2px}
</style>
</head>
<body>
<div class="canvas">

  <svg class="dieline" width="1200" height="883" viewBox="0 0 1200 883" aria-hidden="true">
    <g fill="var(--flap)">
      <path d="M528 52 L590 52 L594 48 L616 48 L620 52 L704 52 L704 176 L528 176 Z"/>
      <rect x="528" y="736" width="176" height="124"/>
      <rect x="404" y="230" width="122" height="90"/>
      <rect x="404" y="592" width="122" height="90"/>
      <rect x="707" y="230" width="123" height="90"/>
      <rect x="707" y="592" width="123" height="90"/>
      <path d="M834 326 L834 262 Q834 204 900 204 L948 204 Q980 204 994 240 L1014 326 Z"/>
      <path d="M834 588 L834 650 Q834 710 900 710 L948 710 Q980 710 994 672 L1014 588 Z"/>
      <path d="M1020 316 L1026 230 Q1110 236 1136 300 L1136 316 Z"/>
      <path d="M1020 596 L1026 682 Q1110 676 1136 612 L1136 596 Z"/>
    </g>
    <rect x="590" y="312" width="54" height="10" fill="var(--tab)"/>
    <rect x="590" y="586" width="54" height="12" fill="var(--tab)"/>
  </svg>

  <!-- top lid end -->
  <div class="panel white" style="left:526px;top:176px;width:181px;height:12px"></div>
  <section class="panel red end-top" style="left:526px;top:188px;width:181px;height:124px">
    <p class="end-copy">
      <span class="line">Lorem ipsum dolor sit amet,</span>
      <span class="line">consectetur adipiscing elit.</span>
      <span class="line">In bibendum malesuada</span>
      <span class="line last">interdum.</span>
    </p>
  </section>

  <!-- left side -->
  <section class="panel white" style="left:404px;top:320px;width:122px;height:272px">
    <div class="mascot" role="img" aria-label="Mascot illustration"></div>
    <p class="side-note">Lorem ipsum dolor sit amet, consectetur adipiscing elit. In bibendum malesuada interdum.</p>
  </section>

  <!-- lid top -->
  <section class="panel" style="left:526px;top:320px;width:181px;height:272px">
    <div class="pattern lid-pattern" role="img" aria-label="Repeating decorative pattern border"></div>
    <div class="label-area" style="left:15px;top:27px;width:152px;height:208px">
      <p class="label-text">Place<br>for label</p>
    </div>
  </section>

  <!-- bottom lid end -->
  <section class="panel red end-bottom" style="left:526px;top:600px;width:181px;height:124px">
    <p class="site">www.petalcrest.com</p>
    <p class="end-copy">
      <span class="line">Lorem ipsum dolor sit amet,</span>
      <span class="line">consectetur adipiscing elit.</span>
      <span class="line">In bibendum malesuada</span>
      <span class="line last">interdum.</span>
    </p>
  </section>
  <div class="panel white" style="left:526px;top:724px;width:181px;height:12px"></div>

  <!-- back side -->
  <section class="panel white" style="left:707px;top:320px;width:123px;height:272px">
    <span class="rule" style="top:0;height:64px"></span>
    <p class="site-vertical">www.petalcrest.com</p>
    <span class="rule" style="top:200px;height:72px"></span>
  </section>

  <!-- front -->
  <section class="panel" style="left:832px;top:326px;width:182px;height:262px">
    <div class="pattern front-pattern" role="img" aria-label="Repeating decorative pattern"></div>
    <div class="brand-label" style="left:56px;top:26px;width:80px;height:198px">
      <p class="brand-name">Petal Crest Box</p>
    </div>
  </section>

  <!-- tagline side -->
  <section class="panel white" style="left:1014px;top:316px;width:122px;height:280px">
    <div class="tagline-box">
      <div class="tagline">
        <span class="tagline-script">Uplift Yourself,</span>
        <span class="tagline-sub">Kind Turn Women</span>
      </div>
    </div>
  </section>

</div>
</body>
</html>
```